Eco friendly Swedish beauty products sold in aluminum bottles - label design needed

We need help in designing a series of stick on labels for 80 ml (2.7 fl. oz.) aluminum bottles containing beauty products such as soaps, shampoo etc. The diameter of the bottle is 36 mm and the body of the bottles measures approx. 106 mm.
It is important for us that the label has a simplistic and clean feel with few colors (and the right ones!) and that the label helps amplify this product being both better and a more sustainable alternative to many of our plastic bottle competitors. The design and label should communicate the feel of an Eco-friendly, sustainable and modern brand of high quality - and with a Swedish concept.
We are using Montserrat font in our materials. Find attached information of preferred colors, the bottles and one example of our logotype. I am also available on e-mail should further information be needed.

Looking forward and very excited to receive your suggestions.
Note that we are expecting to start selling a series of approximately 10 different products where I will need one "master design" and then only smaller changes for each of the different products.

Target Market(s)

People whom are aware and not only look at price tag. Private and commercial market.

Industry/Entity Type

Beauty

Font styles to use
Other font styles liked:
• Montserrat

Requirements
Must have
• It must give the feel of being both better and a more sustainable alternative to many of our plastic bottle competitors.
Nice to have
• Simplistic. Clean. Clear.
Should not have
• Wrong colors, too complex designs.

```html
<!DOCTYPE html>
<html lang="en">
<head>
<meta charset="utf-8">
<title>Klar by Elmsten – Bottle Label Series</title>
<link href="https://fonts.googleapis.com/css2?family=Montserrat:wght@300;400;500&display=swap" rel="stylesheet">
<style>
  :root {
    --paper: #ffffff;
    --ink: #111111;
    --label-black: #000000;
    --copper: #a56a2f;
    --white: #ffffff;
    --alu-light: #e9eaec;
    --alu-mid: #c3c5c9;
    --alu-dark: #8d9095;
  }
  * { box-sizing: border-box; margin: 0; padding: 0; }
  html, body { width: 1200px; height: 849px; overflow: hidden; background: var(--paper); }
  body { position: relative; font-family: "Montserrat", sans-serif; color: var(--ink); }

  .brand-header {
    position: absolute; left: 470px; top: 156px; width: 160px;
    text-align: center; font-size: 13px; font-weight: 400; letter-spacing: 1.5px;
    color: var(--ink);
  }

  /* dimension marks */
  .dim-v { position: absolute; left: 179px; top: 349px; width: 1px; height: 262px; background: var(--ink); }
  .dim-v::before, .dim-v::after { content: ""; position: absolute; left: -4px; width: 9px; height: 1px; background: var(--ink); }
  .dim-v::before { top: 0; } .dim-v::after { bottom: 0; }
  .dim-h { position: absolute; left: 194px; top: 626px; width: 70px; height: 1px; background: var(--ink); }
  .dim-h::before, .dim-h::after { content: ""; position: absolute; top: -4px; width: 1px; height: 9px; background: var(--ink); }
  .dim-h::before { left: 0; } .dim-h::after { right: 0; }
  .dim-label { position: absolute; font-size: 17px; font-weight: 300; }
  .dim-height { left: 117px; top: 470px; }
  .dim-width { left: 202px; top: 634px; }

  /* label */
  .label {
    position: absolute; width: 70px; height: 262px; background: var(--label-black);
    display: flex; flex-direction: column; align-items: center; padding-top: 58px;
  }
  .label .bar { position: absolute; left: 0; top: 0; width: 6px; height: 50px; background: var(--copper); }
  .label .brand, .label .product {
    writing-mode: vertical-rl; white-space: nowrap; line-height: 1.05;
  }
  .label .brand { font-size: 8.5px; letter-spacing: 0.6px; font-weight: 400; }
  .label .divider { width: 1px; height: 12px; margin: 5px 0; }
  .label .product { font-size: 10px; font-weight: 400; }
  .label .volume { position: absolute; right: 6px; bottom: 6px; font-size: 5.5px; font-weight: 500; }

  .tone-copper { color: var(--copper); }
  .tone-white { color: var(--white); }
  .bg-copper { background: var(--copper); }
  .bg-white { background: var(--white); }

  .label-flat { left: 194px; top: 349px; }
  .label-shampoo { left: 356px; top: 352px; }
  .label-conditioner { left: 519px; top: 352px; }
  .label-sanitizer { left: 682px; top: 352px; }

  .bottle { position: absolute; top: 229px; width: 141px; height: 424px; }
  .bottle-1 { left: 316px; } .bottle-2 { left: 479px; } .bottle-3 { left: 642px; }

  .swatch { position: absolute; top: 670px; width: 30px; height: 30px; border-radius: 50%; }
  .swatch.outline { border: 1px solid #bbbbbb; background: var(--white); }
  .print-note { position: absolute; top: 710px; width: 120px; text-align: center; font-size: 17px; font-weight: 300; }

  /* packaging */
  .packaging { position: absolute; left: 806px; top: 203px; width: 218px; height: 439px; background: var(--label-black); }
  .packaging .bar { position: absolute; left: 0; top: 0; width: 17px; height: 186px; background: var(--copper); }
  .packaging .brand {
    position: absolute; left: 103px; top: 114px; writing-mode: vertical-rl;
    font-size: 12.5px; letter-spacing: 1px; color: var(--copper); white-space: nowrap;
  }
  .packaging .rule { position: absolute; left: 74px; top: 276px; width: 68px; height: 1px; background: var(--white); }
  .packaging .product {
    position: absolute; left: 0; right: 0; top: 296px; text-align: center;
    font-size: 19px; line-height: 1; color: var(--copper);
  }
  .packaging .volume { position: absolute; right: 10px; bottom: 10px; font-size: 9px; font-weight: 500; color: var(--copper); }
  .packaging-caption { position: absolute; left: 858px; top: 660px; width: 120px; text-align: center; font-size: 16px; font-weight: 300; letter-spacing: 1.5px; }
</style>
</head>
<body>
  <div class="brand-header">KLAR BY ELMSTEN</div>

  <div class="dim-v"></div>
  <div class="dim-label dim-height">65mm</div>
  <div class="dim-h"></div>
  <div class="dim-label dim-width">17mm</div>

  <div class="label label-flat">
    <div class="bar bg-copper"></div>
    <div class="brand tone-white">KLAR BY ELMSTEN</div>
    <div class="divider bg-copper"></div>
    <div class="product tone-copper">Conditioner &amp;<br>Body Lotion</div>
    <div class="volume tone-copper">80ml</div>
  </div>

  <svg class="bottle bottle-1" viewBox="0 0 141 424" role="img" aria-label="Aluminium 80 ml bottle with screw cap">
    <defs>
      <linearGradient id="alu" x1="0" x2="1">
        <stop offset="0" stop-color="#8d9095"/>
        <stop offset="0.3" stop-color="#e9eaec"/>
        <stop offset="0.6" stop-color="#c3c5c9"/>
        <stop offset="1" stop-color="#8d9095"/>
      </linearGradient>
    </defs>
    <path d="M30,0 h81 v55 C111,75 141,95 141,150 V410 q0,14 -14,14 H14 q-14,0 -14,-14 V150 C0,95 30,75 30,55 Z" fill="url(#alu)"/>
  </svg>
  <svg class="bottle bottle-2" viewBox="0 0 141 424" role="img" aria-label="Aluminium 80 ml bottle with screw cap">
    <path d="M30,0 h81 v55 C111,75 141,95 141,150 V410 q0,14 -14,14 H14 q-14,0 -14,-14 V150 C0,95 30,75 30,55 Z" fill="url(#alu)"/>
  </svg>
  <svg class="bottle bottle-3" viewBox="0 0 141 424" role="img" aria-label="Aluminium 80 ml bottle with screw cap">
    <path d="M30,0 h81 v55 C111,75 141,95 141,150 V410 q0,14 -14,14 H14 q-14,0 -14,-14 V150 C0,95 30,75 30,55 Z" fill="url(#alu)"/>
  </svg>

  <div class="label label-shampoo">
    <div class="bar bg-copper"></div>
    <div class="brand tone-copper">KLAR BY ELMSTEN</div>
    <div class="divider bg-copper"></div>
    <div class="product tone-copper">Hair<br>Shampoo</div>
    <div class="volume tone-copper">80ml</div>
  </div>

  <div class="label label-conditioner">
    <div class="bar bg-white"></div>
    <div class="brand tone-white">KLAR BY ELMSTEN</div>
    <div class="divider bg-white"></div>
    <div class="product tone-white">Conditioner &amp;<br>Body Lotion</div>
    <div class="volume tone-white">80ml</div>
  </div>

  <div class="label label-sanitizer">
    <div class="bar bg-copper"></div>
    <div class="brand tone-white">KLAR BY ELMSTEN</div>
    <div class="divider bg-copper"></div>
    <div class="product tone-copper">Hand<br>Sanitizer</div>
    <div class="volume tone-copper">80ml</div>
  </div>

  <div class="swatch bg-copper" style="left:371px"></div>
  <div class="print-note" style="left:326px">1C Print</div>
  <div class="swatch outline" style="left:534px"></div>
  <div class="print-note" style="left:489px">1C Print</div>
  <div class="swatch bg-copper" style="left:679px"></div>
  <div class="swatch outline" style="left:715px"></div>
  <div class="print-note" style="left:652px">2C Print</div>

  <div class="packaging">
    <div class="bar"></div>
    <div class="brand">KLAR BY ELMSTEN</div>
    <div class="rule"></div>
    <div class="product">Conditioner &amp;<br>Body Lotion</div>
    <div class="volume">80ml</div>
  </div>
  <div class="packaging-caption">PACKAGING</div>
</body>
</html>
```